Healthy Lifestyle Vitamin Supplement Company needs a web site designed.

We are starting a new website for selling quality natural vitamins and supplements online plus providing news and information on healthy living. We DO NOT need any programming done for this site. Just the design in a layered photoshop file. This site needs to communicate that we are the authoritative source for healthy living and a trusted place to buy supplements and information on living a healthy lifestyle.

Triggers On page will be

Trigger set 1
Home - Shop By Brand - Top Sellers - Clearance - Help Center - My Favorites

Trigger set 2
Vitamins and Herbs - Natural Living - Aromatherapy - Coffee and Tea - Health and Beauty - Healthy Foods - Pet Health - Sports and Diet

Triggers Other
Login - Shopping Cart - Checkout - Track Order

Need a search bar in the design

Left side should be categories look at Brelvox.com for example of categories.

Name and domain name is Sunward Meadow Crest

Will also need a logo to go along with that.

Industry/Entity Type

It Company

```html
<!DOCTYPE html>
<html lang="en">
<head>
<meta charset="utf-8">
<title>Sunward Meadow Crest – Natural Vitamins and Supplements</title>
<link rel="stylesheet" href="https://fonts.googleapis.com/css2?family=Open+Sans:wght@400;600;700;800&display=swap">
<style>
:root{
  --green:#8dc63f;
  --green-dark:#6a9f22;
  --blue:#1ea5e3;
  --blue-dark:#1187c0;
  --ink:#333;
  --muted:#777;
  --line:#e1e1e1;
  --topbar:#1f1f1f;
  --footer:#2e2e2e;
  --footer-light:#f0f0f0;
  --red:#e0262a;
  --white:#fff;
}
*{box-sizing:border-box;margin:0;padding:0}
html,body{width:1200px;height:2959px;overflow:hidden}
body{font-family:"Open Sans",Arial,sans-serif;color:var(--ink);background:var(--white);font-size:12px;position:relative}
a{color:inherit;text-decoration:none}
ul{list-style:none}
.wrap{width:984px;margin:0 auto;position:relative}

/* top bar */
.topbar{height:26px;background:var(--topbar);color:#ddd;font-size:10px;font-weight:700;letter-spacing:.3px}
.topbar .wrap{display:flex;justify-content:flex-end;align-items:center;height:26px;gap:8px}
.topbar .sep{color:#777}

/* header */
.header{height:88px}
.header .wrap{display:flex;align-items:center;height:88px}
.logo{display:flex;align-items:center;gap:10px;width:400px}
.logo .dot{width:30px;height:30px;border-radius:50%;background:var(--green)}
.logo .name{font-weight:800;font-size:22px;color:var(--green-dark);letter-spacing:.5px;text-transform:uppercase;line-height:1}
.search{display:flex;width:300px;height:28px;border:1px solid #cfcfcf}
.search span{flex:1;padding:5px 10px;color:#999;font-size:11px}
.search .btn{width:32px;background:var(--blue);display:flex;align-items:center;justify-content:center}
.cart{margin-left:auto;display:flex;align-items:center;gap:8px;font-size:11px}
.cart .checkout{font-weight:700;text-decoration:underline}

.catnav{height:26px;border-bottom:1px solid var(--line)}
.catnav .wrap{display:flex;align-items:center;height:26px;gap:7px;font-size:11px;color:#444}
.catnav .sep{color:#aaa}

.mainnav{margin-top:10px}
.mainnav ul{display:flex;background:var(--green);height:30px}
.mainnav li{width:140px;text-align:center;color:var(--white);font-weight:700;font-size:11.5px;line-height:30px;text-transform:uppercase;border-right:1px solid rgba(255,255,255,.35)}
.mainnav li.active{background:var(--blue)}

/* hero */
.hero{margin-top:16px;height:336px;position:relative;overflow:hidden}
.hero .photo{position:absolute;inset:0;background:linear-gradient(90deg,#c9d6c0 0%,#e7ece4 40%,#f5f6f4 60%,#fafafa 100%)}
.hero .jars{position:absolute;left:80px;top:50px;width:330px;height:230px;border-radius:30px;background:linear-gradient(135deg,#3a7fb8 0%,#e5a12f 45%,#4aa94a 75%,#d35a33 100%);opacity:.55}
.hero h1{position:absolute;right:50px;top:66px;width:440px;font-size:40px;font-weight:800;line-height:1.22;color:#2f2f2f}
.hero .badge{position:absolute;left:28px;top:222px;width:112px;height:112px;border-radius:50%;background:var(--red);color:var(--white);text-align:center;font-weight:800;padding-top:26px;line-height:1.1}
.hero .badge b{display:block;font-size:22px}
.hero .badge span{font-size:13px}
.hero .dots{position:absolute;right:14px;bottom:12px;display:flex;gap:6px}
.hero .dots i{width:9px;height:9px;border-radius:50%;background:#555;display:block}
.hero .dots i.on{background:var(--blue)}

/* category tiles */
.tiles{display:flex;gap:16px;margin-top:16px}
.tile{width:234px}
.tile .pic{height:150px}
.tile .label{background:var(--blue);color:var(--white);font-weight:700;font-size:15px;text-align:center;height:34px;line-height:34px}

/* body */
.main{display:flex;gap:24px;margin-top:38px}
.sidebar{width:226px;border:1px solid var(--line)}
.sidebar h3{font-size:11px;font-weight:800;padding:12px 14px;border-bottom:1px solid var(--line);display:flex;align-items:center;gap:8px;text-transform:uppercase}
.sidebar li{font-size:11px;color:#555;padding:0 14px;height:32px;line-height:32px;border-bottom:1px solid #efefef}
.sidebar li:last-child{border-bottom:0}
.products{flex:1}
.grid{display:grid;grid-template-columns:repeat(3,232px);column-gap:18px;row-gap:20px}
.card{border:1px solid var(--line);height:325px;position:relative;overflow:hidden;text-align:center}
.card h4{text-align:left;font-size:14px;font-weight:700;padding:10px 10px 8px;display:flex;align-items:center;gap:8px}
.card h4 .ic{width:14px;height:14px;border-radius:50%;background:var(--green)}
.card .pic{height:140px;margin:0 40px}
.card .pname{color:var(--blue);font-weight:700;font-size:11px;margin-top:10px;padding:0 12px;line-height:1.35;height:30px}
.card .retail{color:#999;font-size:10px;text-decoration:line-through;margin-top:4px}
.card .price{color:var(--green-dark);font-weight:800;font-size:18px;margin-top:2px}
.card .btns{display:flex;justify-content:center;gap:8px;margin-top:10px}
.card .btns span{width:88px;height:24px;line-height:24px;font-size:10px;font-weight:700;text-transform:uppercase}
.card .shop{background:#e2e2e2;color:#444}
.card .more{background:var(--blue);color:var(--white)}
.ribbon{position:absolute;top:12px;right:-26px;width:100px;transform:rotate(45deg);background:var(--green);color:var(--white);font-size:10px;font-weight:800;line-height:18px}
.pager{display:flex;justify-content:flex-end;gap:6px;margin-top:22px}
.pager span{width:30px;height:30px;border:1px solid #ccc;line-height:28px;text-align:center;font-size:12px}
.pager span.on{background:#555;color:var(--white);border-color:#555}

/* news */
.news{background:var(--green);margin-top:60px;height:112px}
.news .wrap{display:flex;align-items:center;height:112px;gap:30px}
.news h2{width:210px;height:58px;border:2px solid var(--white);color:var(--white);font-size:22px;font-weight:800;text-align:center;line-height:54px;flex:none}
.news p{color:var(--white);font-size:12px;line-height:1.5;text-align:center}

.connect{display:flex;margin-top:24px;height:112px}
.connect section{width:328px}
.connect h5{color:var(--blue);font-size:14px;font-weight:700}
.connect p{font-size:10.5px;color:#555;line-height:1.5;margin-top:4px}
.signup{display:flex;margin-top:12px}
.signup span{width:200px;height:26px;border:1px solid #ccc;font-size:10px;color:#aaa;padding:6px 8px}
.signup b{background:var(--blue);color:var(--white);font-size:10px;padding:0 14px;line-height:26px}
.social{display:flex;gap:14px;margin-top:12px}
.social i{width:34px;height:34px;border-radius:50%;display:block}

/* footer */
.footer{background:var(--footer);height:165px;color:#ccc;margin-top:10px}
.footer .wrap{display:flex;padding-top:26px}
.footer .col{width:200px}
.footer h6{font-size:13px;color:var(--white);font-weight:600;margin-bottom:10px}
.footer li{font-size:10.5px;line-height:1.45}
.footer .flogo{margin-left:auto;display:flex;align-items:center;gap:8px;margin-top:26px;height:40px}
.footer .flogo .dot{width:22px;height:22px;border-radius:50%;background:var(--white)}
.footer .flogo .name{color:var(--white);font-weight:800;font-size:15px;text-transform:uppercase}

.legal{background:var(--footer-light);height:600px}
.legal .wrap{padding-top:38px}
.badges{display:flex;align-items:center;gap:34px;height:54px}
.badges .seal{width:130px;height:44px;border-radius:6px;background:#3d3d3d}
.badges .seal.red{width:150px;background:#b4262a}
.badges .pay{width:190px;height:44px;border-radius:6px;background:#1b4b8a;margin-left:auto}
.badges .card-chip{width:50px;height:34px;border-radius:4px}
.notice{background:var(--white);border:1px solid #ddd;margin-top:30px;padding:14px 60px;text-align:center;font-size:11px;line-height:1.5}
.notice b{font-weight:700}
.fine{font-size:11px;color:#444;line-height:1.55;text-align:center;margin-top:18px;padding:0 20px}
.copy{position:absolute;left:0;right:0;bottom:0;height:36px;background:var(--footer);color:#ccc;font-size:10.5px}
.copy .wrap{line-height:36px}
</style>
</head>
<body>

<div class="topbar"><div class="wrap">
  <span>PHONE : 0123 555 0190</span><span class="sep">|</span><span>LOGIN</span><span class="sep">|</span><span>REGISTER</span><span class="sep">|</span><span>TRACK ORDER</span>
</div></div>

<header class="header"><div class="wrap">
  <div class="logo"><span class="dot"></span><span class="name">Sunward Meadow Crest</span></div>
  <div class="search"><span>Search</span><span class="btn"><svg width="14" height="14" viewBox="0 0 14 14"><circle cx="6" cy="6" r="4.3" fill="none" stroke="#fff" stroke-width="1.8"/><line x1="9.2" y1="9.2" x2="13" y2="13" stroke="#fff" stroke-width="2"/></svg></span></div>
  <div class="cart">
    <svg width="16" height="14" viewBox="0 0 16 14"><path d="M1 1h3l2 8h8l1.5-6H5" fill="none" stroke="#555" stroke-width="1.5"/><circle cx="7" cy="12" r="1.3" fill="#555"/><circle cx="13" cy="12" r="1.3" fill="#555"/></svg>
    <span>My Cart (0)</span><span class="checkout">Checkout</span>
  </div>
</div></header>

<nav class="catnav"><div class="wrap">
  <span>Vitamins and Herbs</span><span class="sep">|</span><span>Natural Living</span><span class="sep">|</span><span>Aromatherapy</span><span class="sep">|</span><span>Coffee and Tea</span><span class="sep">|</span><span>Health and Beauty</span><span class="sep">|</span><span>Healthy Foods</span><span class="sep">|</span><span>Pet Health</span><span class="sep">|</span><span>Sports and Diet</span>
</div></nav>

<nav class="mainnav wrap"><ul>
  <li class="active">Home</li><li>Shop By Brand</li><li>Top Sellers</li><li>Clearance</li><li>Help Center</li><li>My Favorites</li>
</ul></nav>

<section class="hero wrap">
  <div class="photo" role="img" aria-label="Photo of supplement jars on a soft light background"></div>
  <div class="jars" role="img" aria-label="Group of colourful vitamin jars"></div>
  <h1>Selling Quality Natural Vitamins and Supplements</h1>
  <div class="badge"><b>FREE</b><span>Shipping<br>on all orders</span></div>
  <div class="dots"><i class="on"></i><i></i><i></i><i></i></div>
</section>

<section class="tiles wrap">
  <div class="tile"><div class="pic" role="img" aria-label="Photo of coffee and tea cups" style="background:linear-gradient(135deg,#e9ddc8,#a9795a)"></div><div class="label">Coffee &amp; Teas</div></div>
  <div class="tile"><div class="pic" role="img" aria-label="Photo of essential oil bottles" style="background:linear-gradient(135deg,#f0e3b5,#c59a3c)"></div><div class="label">Essential Oils</div></div>
  <div class="tile"><div class="pic" role="img" aria-label="Photo of protein powder" style="background:linear-gradient(135deg,#e6e2dc,#8e7e6a)"></div><div class="label">Protein</div></div>
  <div class="tile"><div class="pic" role="img" aria-label="Photo of fresh healthy vegetables" style="background:linear-gradient(135deg,#b7d77a,#c4472f)"></div><div class="label">New Healthy Foods</div></div>
</section>

<div class="main wrap">
  <aside class="sidebar">
    <h3><svg width="12" height="12" viewBox="0 0 12 12"><circle cx="6" cy="6" r="6" fill="#8dc63f"/></svg>Categories</h3>
    <ul>
      <li>A-B-C-D Vitamins</li><li>Acidophilus/Probiotics</li><li>Amino Acid Supplements</li><li>Antioxidants</li><li>B Vitamins</li><li>B-12 Vitamins</li><li>B-Complex Vitamins</li><li>Babies &amp; Kids</li><li>C Vitamins</li><li>Calcium Supplements</li><li>Co Q-10</li><li>D Vitamins</li><li>Diet &amp; Lifestyle</li><li>Digestive Health</li><li>E Vitamins</li><li>Eye Health</li><li>Fish Oils</li><li>Garcinia Cambogia</li><li>Health &amp; Beauty</li><li>Herbal Supplements</li><li>Joint Support</li><li>L-Carnitine</li><li>Magnesium</li><li>Medicine Cabinet</li><li>Men's Vitamins</li><li>Mental Focus</li><li>Multivitamins</li><li>Omega 3 Products</li><li>Organic, Vegetarian, Non-GMO</li><li>Sexual Health</li><li>Turmeric</li><li>Women's Vitamins</li>
    </ul>
  </aside>

  <div class="products">
    <div class="grid">
      <article class="card"><h4><span class="ic"></span>Heart Health</h4><div class="pic" role="img" aria-label="Amber supplement bottle" style="background:linear-gradient(180deg,#f4f4f4,#b2672c 40%,#7a3d14)"></div><p class="pname">Flush Free Niacin Inositol Nicotinate 1000 mg</p><p class="retail">Retail $35.40</p><p class="price">$22.50</p><div class="btns"><span class="shop">Shop Now</span><span class="more">Read More</span></div></article>
      <article class="card"><h4><span class="ic"></span>Omega-3</h4><div class="pic" role="img" aria-label="Fish oil softgel bottle" style="background:linear-gradient(180deg,#f4f4f4,#c27a2e 40%,#8a4a18)"></div><p class="pname">Maximum Strength Triple Omega 3-6-9 Fish</p><p class="retail">Retail $35.40</p><p class="price">$22.50</p><div class="btns"><span class="shop">Shop Now</span><span class="more">Read More</span></div></article>
      <article class="card"><div class="ribbon">NEW</div><h4><span class="ic"></span>Diet &amp; Lifestyle</h4><div class="pic" role="img" aria-label="White supplement jar" style="background:linear-gradient(180deg,#f6f6f6,#dcdcd4 50%,#9aa87a)"></div><p class="pname">Raspberry Ketones 500 mg</p><p class="retail">Retail $35.40</p><p class="price">$22.50</p><div class="btns"><span class="shop">Shop Now</span><span class="more">Read More</span></div></article>

      <article class="card"><h4><span class="ic"></span>Eye Health</h4><div class="pic" role="img" aria-label="Amber supplement bottle" style="background:linear-gradient(180deg,#f4f4f4,#b2672c 40%,#7a3d14)"></div><p class="pname">Lutein 20 mg with Zeaxanthin</p><p class="retail">Retail $35.40</p><p class="price">$22.50</p><div class="btns"><span class="shop">Shop Now</span><span class="more">Read More</span></div></article>
      <article class="card"><div class="ribbon">NEW</div><h4><span class="ic"></span>Health &amp; Beauty</h4><div class="pic" role="img" aria-label="Softgel supplement bottle" style="background:linear-gradient(180deg,#f4f4f4,#c27a2e 40%,#8a4a18)"></div><p class="pname">Flush Free Facial Oil 1000 mg</p><p class="retail">Retail $35.40</p><p class="price">$22.50</p><div class="btns"><span class="shop">Shop Now</span><span class="more">Read More</span></div></article>
      <article class="card"><h4><span class="ic"></span>Digestive Health</h4><div class="pic" role="img" aria-label="White supplement jar" style="background:linear-gradient(180deg,#f6f6f6,#dcdcd4 50%,#9aa87a)"></div><p class="pname">Probiotic Acidophilus</p><p class="retail">Retail $35.40</p><p class="price">$22.50</p><div class="btns"><span class="shop">Shop Now</span><span class="more">Read More</span></div></article>

      <article class="card"><h4><span class="ic"></span>Heart Health</h4><div class="pic" role="img" aria-label="Amber supplement bottle" style="background:linear-gradient(180deg,#f4f4f4,#b2672c 40%,#7a3d14)"></div><p class="pname">Flush Free Niacin Inositol Nicotinate 1000 mg</p><p class="retail">Retail $35.40</p><p class="price">$22.50</p><div class="btns"><span class="shop">Shop Now</span><span class="more">Read More</span></div></article>
      <article class="card"><h4><span class="ic"></span>Omega-3</h4><div class="pic" role="img" aria-label="Fish oil softgel bottle" style="background:linear-gradient(180deg,#f4f4f4,#c27a2e 40%,#8a4a18)"></div><p class="pname">Maximum Strength Triple Omega 3-6-9 Fish</p><p class="retail">Retail $35.40</p><p class="price">$22.50</p><div class="btns"><span class="shop">Shop Now</span><span class="more">Read More</span></div></article>
      <article class="card"><div class="ribbon">NEW</div><h4><span class="ic"></span>Diet &amp; Lifestyle</h4><div class="pic" role="img" aria-label="White supplement jar" style="background:linear-gradient(180deg,#f6f6f6,#dcdcd4 50%,#9aa87a)"></div><p class="pname">Raspberry Ketones 500 mg</p><p class="retail">Retail $35.40</p><p class="price">$22.50</p><div class="btns"><span class="shop">Shop Now</span><span class="more">Read More</span></div></article>
    </div>
    <div class="pager"><span class="on">1</span><span>2</span><span>3</span><span>4</span><span>5</span><span>6</span><span>&gt;&gt;</span></div>
  </div>
</div>

<section class="news"><div class="wrap">
  <h2>IN THE NEWS</h2>
  <p>Lorem ipsum dolor sit amet, consectetur adipisicing elit, sed do eiusmod tempor incididunt ut labore et dolore magna aliqua. Ut enim ad minim veniam, quis nostrud exercitation ullamco laboris nisi ut aliquip ex ea commodo consequat. Duis aute irure dolor in reprehenderit in voluptate velit esse cillum.</p>
</div></section>

<section class="connect wrap">
  <section><h5>Email Sign-Up</h5><p>Be the first to receive special discounts</p><div class="signup"><span>Enter your email ID</span><b>SUBSCRIBE</b></div></section>
  <section><h5>Contact Us</h5><p>27 Orchard Row, Fernvale 40218<br>Phone:+123 555 0148<br>Email: info@sunwardmeadowcrest.com</p></section>
  <section><h5>Stay Connected</h5><p>Find out what people are saying</p>
    <div class="social"><i style="background:#1ea5e3" aria-label="Social network one"></i><i style="background:#3b5998" aria-label="Social network two"></i><i style="background:#1a7bbf" aria-label="Social network three"></i><i style="background:#d64032" aria-label="Social network four"></i></div>
  </section>
</section>

<footer class="footer"><div class="wrap">
  <div class="col"><h6>Company Info</h6><ul><li>About Us</li><li>Affiliate Program</li><li>Contact Us</li><li>Quality Guarantee</li><li>CSPR</li><li>International Distribution</li></ul></div>
  <div class="col"><h6>Customer Service</h6><ul><li>Price Match Guarantee</li><li>Coupon Policy</li><li>Help Center</li></ul></div>
  <div class="col"><h6>My Account</h6><ul><li>Log In</li><li>Auto Delivery</li><li>Create Account</li><li>My Favorites</li><li>Order History</li><li>Track Order</li><li>Sweepstakes</li></ul></div>
  <div class="col"><h6>Shipping &amp; Returns</h6><ul><li>International Shipping</li><li>Lost or Damaged</li><li>Return Policy</li><li>Shipping Information</li></ul></div>
  <div class="flogo"><span class="dot"></span><span class="name">Sunward Meadow Crest</span></div>
</div></footer>

<section class="legal"><div class="wrap">
  <div class="badges">
    <span class="seal" aria-label="Privacy certification badge"></span>
    <span class="seal red" aria-label="Security certification badge"></span>
    <span class="pay" aria-label="Online payment badge"></span>
    <span class="card-chip" style="background:#e8731d" aria-label="Payment card"></span>
    <span class="card-chip" style="background:#1a3d8f" aria-label="Payment card"></span>
    <span class="card-chip" style="background:#2d8fd3" aria-label="Payment card"></span>
    <span class="card-chip" style="background:#f08a1d" aria-label="Payment card"></span>
  </div>
  <div class="notice"><b>* Sunward Meadow Crest provides these articles for information only. They are not approved or recommended by us, do not provide medical advice, diagnosis, or treatment, and are not meant to replace professional medical advice or apply to any products.</b></div>
  <p class="fine">**These statements have not been evaluated by the Food and Drug Administration. These products are not intended to diagnose, treat, cure or prevent any disease.</p>
  <p class="fine">The information provided on this site is intended for your general knowledge only and is not a substitute for professional medical advice or treatment for specific medical conditions. Always seek the advice of your physician or other qualified health care provider with any questions you may have regarding a medical condition. The information on this website is not intended to diagnose, treat, cure or prevent any disease. Never disregard medical advice or delay in seeking it because of something you have read on the Sunward Meadow Crest site. Product sold on this site are for personal use and not for resale. All orders placed through this website are subject to Sunward Meadow Crest acceptance, in its sole discretion. This means that Sunward Meadow Crest may refuse to accept, or may cancel, any order, whether or not it has been confirmed, without liability to you or any third party. Sunward Meadow Crest reserves the right to discontinue any program or offer.</p>
  <p class="fine">If you would like to unsubscribe from future Sunward Meadow Crest emails, please click here to unsubscribe.</p>
  <p class="fine">* Same item, same size Sunward Meadow Crest brand products, discount already reflected in the applicable product price. Certain products, including clearance section items, may be excluded. All products subject to availability. To expedite orders, we may substitute smaller bottles if ordered quantity is out of stock. Terms and conditions subject to change. Free Shipping offers apply within the contiguous 48 U.S. states; will automatically apply to your cart at checkout; not valid on orders.</p>
</div></section>

<div class="copy"><div class="wrap">Copyright 2014 Sunward Meadow Crest, Inc. | Customer Service 1123-555-0162 | Privacy Policy | Terms of Use</div></div>

</body>
</html>
```